Need Print and Packaging Designs for screen protector brand

Need unique packaging design for the product (screen guard) of brand- Quillet.

Please see the attached file for color suggestion from me, and current design

Color combination suggestions - Though you would be a master at these, these are just for reference and to express what could look good, and you can use your own creative ideas too.
Current design - includes content, product logo (needs to be changed), brand logo(needs to be changed)

See a product sample also included in the zip file

use 3-4 colors at most.
Lighter shades are really preferred with a great combination.
Simplistic design that makes the packaging really stand apart

Need not have more than 4 colors.
The design should not look like splashed with colors unnecessarily.

Use a neutral design for a smartphone in design(it should not represent any specific model or brand, remove any logos or branding).

Your Job:

1. Create design for main packaging using your skills, referring to competitor products and color combinations that are the best and look simple yet elegant.
2. Create logo or modify the existing text written product logo
3. Create one or modify the brand logo
4. The print and packing is on a matte paper so you can plan accordingly for colors.
5. Brand name will have a laminated finish on top for actual packaging, do what you can , to make it look appealing.
6. Preferably black or white background, anything else if looks good is fine with me.

I appreciate your time, patience and talent.
Please PM me with questions, suggestions or anything you would like to know.
Attached is the File for reference.

```html
<!DOCTYPE html>
<html lang="en">
<head>
<meta charset="utf-8">
<title>Quillet screen protector packaging – dieline</title>
<link href="https://fonts.googleapis.com/css2?family=Open+Sans:ital,wght@0,400;0,600;0,700;1,400&display=swap" rel="stylesheet">
<style>
  :root{
    --paper:#ffffff;
    --cut:#555b60;
    --slate-dark:#4b5964;
    --slate-mid:#6f7d88;
    --slate-light:#a3aeb6;
    --ink:#1f262c;
    --white:#ffffff;
    --sky:#5cc6f0;
    --sky-pale:#c4eaf9;
    --badge:#3fb3e6;
    --device:#1c2025;
  }
  html,body{margin:0;padding:0;background:var(--paper);overflow:hidden}
  .canvas{width:848px;height:1200px;position:relative;overflow:hidden;background:var(--paper);font-family:"Open Sans",Arial,sans-serif}
  .sheet{position:absolute;left:0;top:0;width:905px;height:1280px;transform:scale(0.9375);transform-origin:0 0}
  .dieline{position:absolute;left:0;top:0}

  .panel{position:absolute;left:297px;width:307px;overflow:hidden}
  .panel--back{top:85px;height:575px;transform:rotate(180deg);
    background:radial-gradient(ellipse 70% 55% at 50% 60%,var(--slate-light),var(--slate-mid) 60%,var(--slate-dark));}
  .panel--front{top:660px;height:575px;
    background:radial-gradient(ellipse 80% 40% at 55% 15%,#7d8a94,var(--slate-dark) 75%);}

  .hang-hole{position:absolute;left:103px;width:100px;height:32px;background:var(--paper);
    clip-path:polygon(20% 0,80% 0,100% 60%,90% 100%,10% 100%,0 60%)}

  /* back panel (printed upside down) */
  .back-heading{position:absolute;left:22px;margin:0;font-weight:700;color:var(--ink);font-size:13px;line-height:16px}
  .feature-list{position:absolute;left:24px;top:88px;width:262px;margin:0;padding:0 0 0 16px;
    font-size:8.8px;line-height:12.3px;color:var(--ink)}
  .feature-list li{padding-left:2px}

  .no-badges{position:absolute;top:216px;left:0;width:307px;height:46px}
  .no-badge{position:absolute;top:0;width:80px;margin-left:-40px;text-align:center}
  .no-badge__ring{width:30px;height:30px;margin:0 auto;border:3px solid var(--badge);border-radius:50%;
    background:rgba(255,255,255,.15);color:var(--white);font-weight:700;font-size:11px;line-height:22px}
  .no-badge__label{display:block;margin-top:-6px;font-size:8.5px;line-height:10px;font-weight:600;color:var(--ink)}

  .steps{position:absolute;left:33px;top:285px;margin:0;padding:0;list-style:none}
  .step{display:flex;align-items:flex-start;height:55px}
  .step-art{width:58px;height:42px;flex:none;border:1px solid #e5e9ec;border-radius:3px;
    background:linear-gradient(135deg,#c4ccd2,#9aa6ae);position:relative}
  .step-art i{position:absolute;left:3px;bottom:3px;width:9px;height:9px;border-radius:50%;background:var(--white);
    font-style:normal;font-size:7px;line-height:9px;text-align:center;color:var(--ink);font-weight:700}
  .step p{margin:3px 0 0 22px;width:176px;font-size:8.6px;line-height:12px;color:var(--ink)}
  .step p b{font-weight:400;margin-right:8px}

  .tear-tab{position:absolute;left:24px;top:478px;width:258px;height:112px;border:1px dashed #d7dde2;border-top:none;border-radius:0 0 10px 10px}
  .tear-notch{position:absolute;left:128px;top:446px;width:50px;height:32px;border:1px dashed #d7dde2;border-bottom:none;border-radius:25px 25px 0 0;background:rgba(255,255,255,.12);text-align:center}
  .tear-notch span{display:block;font-size:6px;font-weight:700;color:var(--ink);margin-top:6px}
  .tear-notch svg{display:block;margin:1px auto 0}
  .tear-line{position:absolute;left:24px;top:478px;width:104px;border-top:1px dashed #d7dde2}
  .tear-line--r{left:178px}
  .contents-label{position:absolute;left:36px;top:485px;font-size:8px;color:var(--ink);margin:0}
  .content-item{position:absolute;top:500px;text-align:center;font-size:7px;line-height:8px;color:var(--ink)}
  .protector-chip{width:28px;height:34px;border-radius:4px;background:#34393e;margin:0 auto 3px}
  .cloth-chip{width:26px;height:26px;background:#40474d;margin:4px auto 7px;outline:2px dotted #40474d;outline-offset:-1px}
  .maker{position:absolute;left:168px;top:488px;margin:0;font-size:7.6px;line-height:9.2px;color:var(--ink)}
  .maker b{font-weight:700}
  .care-marks{position:absolute;left:168px;top:560px;display:flex;gap:10px}
  .care-marks i{width:13px;height:13px;border:1.4px solid #30363b;border-radius:50%;box-sizing:border-box}
  .care-marks i:last-child{border-radius:2px}

  /* front panel */
  .brand{position:absolute;left:19px;top:40px;display:flex;align-items:center;gap:6px}
  .brand-dot{width:36px;height:36px;border-radius:50%;background:var(--badge)}
  .brand-name{color:var(--white);font-weight:600;font-size:13px}
  .product-name{position:absolute;right:24px;top:58px;margin:0;font-weight:600;font-size:40px;line-height:40px;color:var(--white);text-transform:lowercase;letter-spacing:-.5px}
  .tagline{position:absolute;right:22px;top:104px;margin:0;font-style:italic;font-size:10.5px;color:var(--white)}
  .availability{position:absolute;right:22px;top:119px;margin:0;font-weight:700;font-size:8.6px;color:var(--sky)}
  .halo{position:absolute;left:-70px;top:140px;width:430px;height:430px;border-radius:50%;background:rgba(255,255,255,.07)}
  .device-visual{position:absolute;left:36px;top:142px;width:198px;height:302px;border-radius:12px;
    background:linear-gradient(160deg,#3a4354,#2a3140 55%,var(--device))}
  .benefits{position:absolute;right:16px;top:360px;margin:0;padding:0;list-style:none;transform:rotate(11deg);transform-origin:100% 0}
  .benefits li{display:flex;justify-content:flex-end;align-items:center;gap:8px;height:26.5px;color:var(--white);font-weight:600;font-size:9.6px}
  .benefits svg{flex:none}
  .finish-band{position:absolute;left:0;bottom:0}
  .finish-label{position:absolute;left:10px;bottom:9px;margin:0;font-size:15px;line-height:18px;color:var(--ink)}
</style>
</head>
<body>
<div class="canvas">
  <div class="sheet">
    <svg class="dieline" width="905" height="1280" viewBox="0 0 905 1280" aria-hidden="true">
      <g fill="var(--paper)" stroke="var(--cut)" stroke-width="1">
        <polygon points="310,38 588,38 604,85 297,85"/>
        <polygon points="297,85 250,112 250,635 297,660"/>
        <polygon points="604,85 650,112 650,635 604,660"/>
        <polygon points="297,112 250,112 250,140 297,140" fill="none"/>
        <polygon points="604,112 650,112 650,140 604,140" fill="none"/>
        <polygon points="297,610 250,610 250,635 297,635" fill="none"/>
        <polygon points="604,610 650,610 650,635 604,635" fill="none"/>
        <rect x="297" y="85" width="307" height="1150" fill="none"/>
      </g>
    </svg>

    <section class="panel panel--back" aria-label="Back panel">
      <div class="hang-hole" style="top:28px"></div>
      <h2 class="back-heading" style="top:66px">Product Description</h2>
      <ol class="feature-list">
        <li>High Transparency of up to 97% preserves the high resolution and vivid colors of your display.</li>
        <li>Anti-scratch coating of hardness 3H protects from wear and tear from sharp objects.</li>
        <li>Easy Removal with no residue or glue traces.</li>
        <li>Washable and reusable multiple times.</li>
        <li>Precise dimension &nbsp;and perfect German machinecut.</li>
        <li>Anti-reflection against sun and other light sources</li>
        <li>Dust repellant, keps it as good as new each day.</li>
        <li>Ultra high sensitivity, comparable to bare screen.</li>
      </ol>
      <div class="no-badges">
        <div class="no-badge" style="left:68px"><div class="no-badge__ring">NO</div><span class="no-badge__label">Scratches</span></div>
        <div class="no-badge" style="left:156px"><div class="no-badge__ring">NO</div><span class="no-badge__label">Finger marks</span></div>
        <div class="no-badge" style="left:243px"><div class="no-badge__ring">NO</div><span class="no-badge__label">Glare</span></div>
      </div>
      <h2 class="back-heading" style="top:264px">How to apply</h2>
      <ol class="steps">
        <li class="step"><div class="step-art" role="img" aria-label="Illustration: wiping the device screen clean"><i>1</i></div>
          <p><b>1.</b>Clean the device screen and make sure the surface is completely dry before you apply the screen protector.</p></li>
        <li class="step"><div class="step-art" role="img" aria-label="Illustration: peeling the small mask portion"><i>2</i></div>
          <p><b>2.</b>Peel off the small portion of the mask labeled step 1 (This side is applied to the screen)</p></li>
        <li class="step"><div class="step-art" role="img" aria-label="Illustration: aligning and brushing down the protector"><i>3</i></div>
          <p><b>3.</b>Align and apply the exposed portion along one side of the screen, lift and reapply until correct, peel off the rest of the mask and slowly brush down.</p></li>
      </ol>
      <div class="tear-line"></div><div class="tear-line tear-line--r"></div>
      <div class="tear-notch"><span>Tear off here</span>
        <svg width="10" height="14" viewBox="0 0 10 14"><path d="M5 14V5M1 6l4-5 4 5" fill="none" stroke="var(--ink)" stroke-width="2"/></svg>
      </div>
      <div class="tear-tab"></div>
      <p class="contents-label">Contents:</p>
      <div class="content-item" style="left:34px"><div class="protector-chip"></div>Screen Pro+<br>Anti-Scratch</div>
      <div class="content-item" style="left:92px"><div class="cloth-chip"></div>Cleaning<br>Cloth</div>
      <p class="maker">Pkd. &amp; Mfd. by<br><b>norvoshop</b><br>www.norvoshop.com/feedback<br><b>Includes:</b><br>1pc. screen protector<br>1pc. cleaning cloth</p>
      <div class="care-marks"><i></i><i></i><i></i><i></i></div>
    </section>

    <section class="panel panel--front" aria-label="Front panel">
      <div class="hang-hole" style="top:16px"></div>
      <div class="halo"></div>
      <div class="brand"><span class="brand-dot"></span><span class="brand-name">Norvo</span></div>
      <h1 class="product-name">Quillet</h1>
      <p class="tagline">The second skin for your touch screen devices</p>
      <p class="availability">Available for all popular mobile phones and tablets</p>
      <div class="device-visual" role="img" aria-label="Product photo: smartphone with screen protector applied"></div>
      <ul class="benefits">
        <li>Scratch resistant<svg width="20" height="20" viewBox="0 0 20 20"><circle cx="10" cy="10" r="8.5" fill="none" stroke="#fff" stroke-width="1.6"/><path d="M4 4l12 12" stroke="#fff" stroke-width="1.6"/></svg></li>
        <li>Anti-Fingerprint<svg width="20" height="20" viewBox="0 0 20 20"><circle cx="10" cy="10" r="8.5" fill="none" stroke="#fff" stroke-width="1.6"/><path d="M4 4l12 12" stroke="#fff" stroke-width="1.6"/></svg></li>
        <li>No sticky glue<svg width="20" height="20" viewBox="0 0 20 20"><circle cx="10" cy="10" r="8.5" fill="none" stroke="#fff" stroke-width="1.6"/><path d="M4 4l12 12" stroke="#fff" stroke-width="1.6"/></svg></li>
        <li>Non Reflective<svg width="20" height="20" viewBox="0 0 20 20"><circle cx="10" cy="10" r="8.5" fill="none" stroke="#fff" stroke-width="1.6"/><circle cx="10" cy="10" r="3" fill="#fff"/><path d="M4 4l12 12" stroke="#fff" stroke-width="1.6"/></svg></li>
        <li>Precise dimensions<svg width="20" height="20" viewBox="0 0 20 20"><path d="M2 7l4-4h8l4 4-8 10z M2 7h16" fill="none" stroke="#fff" stroke-width="1.5"/></svg></li>
        <li>Truly washable<svg width="20" height="20" viewBox="0 0 20 20"><path d="M10 2C7 7 5 10 5 13a5 5 0 0 0 10 0c0-3-2-6-5-11z" fill="#fff"/></svg></li>
        <li>Ultra smooth touch<svg width="20" height="20" viewBox="0 0 20 20"><rect x="8" y="8" width="5" height="11" rx="2.5" fill="#fff"/><path d="M10.5 2v3M5 4l2 2M16 4l-2 2M3 9h3M15 9h3" stroke="#fff" stroke-width="1.5"/></svg></li>
      </ul>
      <svg class="finish-band" width="307" height="80" viewBox="0 0 307 80" aria-hidden="true">
        <polygon points="0,2 307,52 307,60 0,10" fill="var(--sky-pale)"/>
        <polygon points="0,10 307,60 307,80 0,80" fill="var(--sky)"/>
      </svg>
      <p class="finish-label">anti-glare | matte</p>
    </section>
  </div>
</div>
</body>
</html>
```